Mortgage broker flyer

I need a flyer to advertise who we are, what we do and why people should use us. and with a call to action. Our service is free, and we have over 35 different lenders that we can source loans from. we offer a mobile service. we will visit people anywhere anytime to discuss their needs. The flyers are to be placed in real estate agencies as well as put in people's letter boxes

Target Market(s)

clients looking at purchasing property - going through open homes.

Industry/Entity Type

Finance

Colors
add136
cadf82
aaaaaa
959595

Requirements
Must have
• Service is free
• won KMR broker of the year 2014,2015
• Verosta insurance - Free 90 days building insurance through Verosta
• Logo colours

```html
<!DOCTYPE html>
<html lang="en">
<head>
<meta charset="utf-8">
<title>Brightway Finance Solutions – Flyer</title>
<link href="https://fonts.googleapis.com/css2?family=Questrial&family=Montserrat:wght@700&display=swap" rel="stylesheet">
<style>
  :root{
    --green:#add136;
    --green-light:#cadf82;
    --grey:#aaaaaa;
    --grey-dark:#959595;
    --backdrop:#c9cacc;
  }
  *{box-sizing:border-box;margin:0;padding:0}
  html,body{width:1200px;height:982px;overflow:hidden;background:var(--backdrop)}
  body{font-family:"Questrial",Arial,sans-serif;position:relative}
  .flyer{
    position:absolute;left:282px;top:36px;width:636px;height:910px;
    background:linear-gradient(160deg,#f7f7f7 0%,#fff 45%,#f2f2f2 100%);
    box-shadow:0 14px 30px rgba(0,0,0,.25);overflow:hidden;
  }
  .header{
    position:absolute;left:0;top:0;width:100%;height:150px;background:#f4f4f4;
    border-bottom:1px solid #e2e2e2;display:flex;align-items:center;padding-left:60px;gap:22px;
  }
  .brand-mark{width:64px;height:64px;border-radius:50%;background:var(--green)}
  .brand-name{font-size:46px;line-height:1;color:var(--green)}
  .brand-sub{font-size:34px;color:var(--grey-dark);margin-top:4px}
  .headline{
    position:absolute;left:60px;top:192px;font-family:"Montserrat",Arial,sans-serif;
    font-size:26px;line-height:32px;letter-spacing:-1px;color:var(--green);white-space:nowrap;
  }
  .subline{position:absolute;left:62px;top:230px;font-size:18px;line-height:22px;color:var(--grey-dark);letter-spacing:.3px;white-space:nowrap}
  .services{position:absolute;left:70px;top:298px;list-style:none}
  .services li{font-size:34px;color:var(--grey);line-height:46px;white-space:nowrap}
  .services li::before{content:"";display:inline-block;width:8px;height:8px;border-radius:50%;background:var(--green);margin:0 14px 8px 0}
  .services .free{color:var(--green);font-family:"Montserrat",Arial,sans-serif;font-size:30px}
  .credentials{position:absolute;left:62px;top:516px;font-size:15px;color:var(--grey-dark);line-height:22px;white-space:nowrap}
  .partner{position:absolute;left:62px;top:600px;display:flex;align-items:center;gap:14px}
  .partner-badge{width:86px;height:86px;border-radius:50%;background:#d9d9d9}
  .partner-name{font-size:20px;color:#333;line-height:24px}
  .green-band{position:absolute;left:0;bottom:0;width:636px;height:380px}
  .photo{
    position:absolute;left:372px;top:580px;width:248px;height:240px;
    background:linear-gradient(180deg,#3a3a3a 0%,#1c1c1c 100%);border-radius:4px;
  }
  .contact{position:absolute;left:62px;bottom:40px;list-style:none;color:#fff;font-size:19px}
  .contact li{display:flex;align-items:center;gap:14px;line-height:34px;white-space:nowrap}
  .contact svg{width:20px;height:20px;flex:none}
</style>
</head>
<body>
  <main class="flyer">
    <header class="header">
      <div class="brand-mark"></div>
      <div>
        <div class="brand-name">Brightway</div>
        <div class="brand-sub">Finance Solutions</div>
      </div>
    </header>

    <h1 class="headline">WE'LL FIND YOU THE RIGHT LOAN</h1>
    <p class="subline">FROM OVER 35 LENDERS AT NO COST TO YOU.</p>

    <ul class="services">
      <li>Get a <span class="free">FREE</span> property report!</li>
      <li>Check our latest rates.</li>
      <li>Apply online.</li>
      <li>Get Pre-Approved Today!</li>
    </ul>

    <p class="credentials">Won KMR broker of the year 2014,2015<br>
      Verosta insurance: Free 90 days building insurance through Verosta</p>

    <svg class="green-band" viewBox="0 0 636 380" aria-hidden="true">
      <defs>
        <linearGradient id="bandFill" x1="0" y1="1" x2="1" y2="0">
          <stop offset="0" stop-color="#add136"/>
          <stop offset="1" stop-color="#9cc531"/>
        </linearGradient>
      </defs>
      <polygon points="0,230 636,0 636,380 0,380" fill="url(#bandFill)"/>
    </svg>

    <div class="partner">
      <div class="partner-badge"></div>
      <div class="partner-name"><strong>Southern</strong><br>Home Lending</div>
    </div>

    <div class="photo" role="img" aria-label="Photo of the two brokers in dinner suits holding their award trophy"></div>

    <ul class="contact">
      <li><svg viewBox="0 0 20 20"><circle cx="10" cy="10" r="8" fill="none" stroke="#fff" stroke-width="1.6"/><path d="M2 10h16M10 2c3 3 3 13 0 16M10 2c-3 3-3 13 0 16" fill="none" stroke="#fff" stroke-width="1.4"/></svg>www.brightwayfs.com.au</li>
      <li><svg viewBox="0 0 20 20"><rect x="2" y="4" width="16" height="12" fill="none" stroke="#fff" stroke-width="1.6"/><path d="M2 4l8 7 8-7" fill="none" stroke="#fff" stroke-width="1.6"/></svg>info@brightwayfs.com.au</li>
      <li><svg viewBox="0 0 20 20"><path d="M5 2l3 4-2 2c1 3 3 5 6 6l2-2 4 3-2 3C9 18 2 11 2 4z" fill="#fff"/></svg>0739 146 208 • 0412 637 915</li>
    </ul>
  </main>
</body>
</html>
```